Plivoro ( A new twist on task management )

We need modern, elegant, and clean (Material Design) on screens, buttons, and icons.

It is a (smart) task management application which helps the users to get notified and track task completion hassle free; Using notification profiles they create.

The interface of this application should be very simple and color schemes should be contemporary as long as they don’t make reading short text hard.

Following Material Design guidelines, the prefered font style is Roboto
Updates

Target Market(s)

Everyone from 13+

Industry/Entity Type

Software

Logo Text

Plivoro

Font styles to use
Other font styles liked:
• Roboto

```html
<!DOCTYPE html>
<html lang="en">
<head>
<meta charset="utf-8">
<title>Plivoro – Task Screens</title>
<link href="https://fonts.googleapis.com/css2?family=Roboto:ital,wght@0,300;0,400;0,500;0,700;1,400&display=swap" rel="stylesheet">
<style>
  :root{
    --bg:#cfe9f7;
    --navy:#0d2a78;
    --navy-deep:#0a2266;
    --ink:#3b5a86;
    --ink-dark:#0f2760;
    --page:#dcefff;
    --band:#c7d8e6;
    --divider:#a9c3d9;
    --fab:#1a9be6;
    --cyan:#00bcf2;
    --tab-on:#2d9cdb;
    --tab-off:#86cdef;
    --confirm:#b4c8dc;
    --key-board:#3e68b4;
    --key:#6f95d6;
    --key-text:#ffffff;
    --toggle-on:#1d4f9c;
    --toggle-off:#7c8a96;
    --map-a:#ece6d8;
    --map-b:#d9dcc2;
    --white:#ffffff;
  }
  *{box-sizing:border-box;margin:0;padding:0}
  html,body{width:809px;height:1200px;overflow:hidden}
  body{background:var(--bg);font-family:'Roboto',sans-serif;position:relative}
  .icons{position:absolute;width:0;height:0}
  .screen{position:absolute;width:320px;height:569px;background:var(--page);overflow:hidden;box-shadow:0 6px 20px rgba(10,40,90,.18)}
  .s1{left:50px;top:30px}.s2{left:439px;top:30px}.s3{left:50px;top:600px}.s4{left:439px;top:600px}

  .status{position:absolute;left:0;top:0;width:100%;height:12px;background:var(--white);font-size:8px;color:#222;display:flex;align-items:center;justify-content:space-between;padding:0 6px}
  .header{position:absolute;left:0;top:12px;width:100%;height:106px;background:var(--navy);text-align:center;color:var(--white)}
  .avatar{position:absolute;left:133px;top:8px;width:54px;height:54px;border-radius:50%;border:2px solid var(--white);background:radial-gradient(circle at 40% 40%,#f2b6c4,#c8324e 55%,#5a2a6b)}
  .user-name{position:absolute;top:65px;width:100%;font-size:14px;font-weight:500}
  .user-place{position:absolute;top:83px;width:100%;font-size:10px;color:#c5d3f0}
  .fab{position:absolute;left:271px;top:99px;width:36px;height:36px;border-radius:50%;background:var(--fab);box-shadow:0 2px 5px rgba(0,0,0,.3);display:flex;align-items:center;justify-content:center;z-index:3}
  .fab svg{width:18px;height:18px}

  .nav{position:absolute;left:0;width:100%;height:32px;background:var(--band);display:flex;align-items:center}
  .nav-back{position:absolute;left:22px;font-size:11px;color:var(--ink-dark);display:flex;align-items:center;gap:3px}
  .nav-back svg{width:8px;height:12px}
  .nav-title{width:100%;text-align:center;font-size:14px;color:var(--ink);font-weight:400}

  .task-list{position:absolute;left:0;top:150px;width:100%}
  .task{position:relative;border-bottom:1px solid var(--divider);display:flex;align-items:center}
  .task-play{position:absolute;left:27px;width:9px;height:12px}
  .task-label{position:absolute;left:50px;font-size:14px;color:var(--ink)}
  .task.is-running .task-label{font-weight:700;color:var(--ink-dark);top:24px}
  .task-timer{position:absolute;left:50px;top:44px;font-size:10px;font-weight:500;color:var(--ink-dark)}
  .task-stop{position:absolute;left:27px;top:28px;width:11px;height:11px;background:var(--ink-dark)}
  .task-pause{position:absolute;left:28px;top:47px;width:9px;height:10px}
  .task-icons .ic{position:absolute;width:20px;height:20px}
  .ic-a{left:221px}.ic-b{left:254px}.ic-c{left:289px}
  .search-bar{position:absolute;left:0;top:524px;width:100%;height:45px;background:var(--cyan);display:flex;align-items:center;justify-content:center}
  .search-bar svg{width:30px;height:30px}

  .field{position:absolute;border:1.5px solid var(--tab-on);background:var(--page);font-size:10px;font-style:italic;color:var(--ink);display:flex;align-items:center;padding-left:12px}
  .field-profile{left:25px;top:166px;width:267px;height:35px;border-radius:18px}
  .section-title{position:absolute;top:233px;width:100%;text-align:center;font-size:14px;font-weight:700;color:var(--ink-dark)}
  .tabs{position:absolute;left:0;top:261px;width:100%;height:36px;display:flex}
  .tab{flex:1;display:flex;align-items:center;justify-content:center;font-size:14px;color:var(--white)}
  .tab-on{background:var(--tab-on)}.tab-off{background:var(--tab-off)}
  .option{position:absolute;left:25px;font-size:14px;color:var(--ink-dark)}
  .toggle{position:absolute;left:254px;width:35px;height:16px;border-radius:8px}
  .toggle::after{content:"";position:absolute;top:1px;width:14px;height:14px;border-radius:50%;background:var(--white);box-shadow:0 1px 2px rgba(0,0,0,.35)}
  .toggle-on{background:var(--toggle-on)}.toggle-on::after{right:1px}
  .toggle-off{background:var(--toggle-off)}.toggle-off::after{right:1px}
  .line{position:absolute;height:1px;background:#7fa6c8}
  .action-bar{position:absolute;left:0;width:100%;height:46px;display:flex}
  .action{flex:1;display:flex;align-items:center;justify-content:center}
  .action svg{width:34px;height:34px}
  .action-ok{background:var(--confirm)}.action-cancel{background:var(--navy)}

  .map{position:absolute;left:0;top:56px;width:100%;height:456px;background:linear-gradient(160deg,var(--map-a),var(--map-b) 60%,var(--map-a))}
  .radius-bar{position:absolute;left:0;top:512px;width:100%;height:57px;background:var(--navy);display:flex;align-items:center;color:var(--white)}
  .radius-label{position:absolute;left:18px;font-size:14px;font-weight:300}
  .slider{position:absolute;left:128px;width:128px;height:3px;background:#9aa8c4;border-radius:2px}
  .slider-fill{position:absolute;left:0;top:0;width:78px;height:3px;background:var(--fab)}
  .slider-knob{position:absolute;left:72px;top:-5px;width:13px;height:13px;border-radius:50%;background:var(--fab)}
  .radius-value{position:absolute;left:267px;font-size:11px;font-weight:500}

  .spacer-band{position:absolute;left:0;top:118px;width:100%;height:33px;background:var(--band)}
  .field-task{left:26px;top:231px;width:267px;height:38px;border-radius:0}
  .rule{position:absolute;left:0;top:283px;width:100%;height:1px;background:var(--divider)}
  .profile-pick{position:absolute;width:50px;height:36px;display:flex;align-items:center;justify-content:center}
  .pick-pin{left:182px;top:293px;background:var(--cyan)}
  .pick-lock{left:242px;top:293px;background:#8c949c}
  .profile-pick svg{width:20px;height:20px}

  .keyboard{position:absolute;left:0;top:367px;width:100%;height:202px;background:var(--key-board);padding:8px 3px 0}
  .key-row{display:flex;justify-content:center;gap:5px;margin-bottom:17px}
  .key{width:27px;height:36px;border-radius:5px;background:var(--key);color:var(--key-text);font-size:20px;font-weight:300;display:flex;align-items:center;justify-content:center}
  .key-wide{width:40px;font-size:14px}
  .key-space{width:122px;font-size:14px}
  .key-return{width:72px;font-size:14px}
  .key svg{width:18px;height:18px}
</style>
</head>
<body>

<svg class="icons" aria-hidden="true">
  <defs>
    <symbol id="i-play" viewBox="0 0 9 12"><path d="M0 0 9 6 0 12Z" fill="#0f2760"/></symbol>
    <symbol id="i-pause" viewBox="0 0 9 10"><rect x="1" width="2.5" height="10" fill="#0f2760"/><rect x="5.5" width="2.5" height="10" fill="#0f2760"/></symbol>
    <symbol id="i-pushpin" viewBox="0 0 24 24"><path d="M14 2l8 8-2 1-3-1-4 4 1 4-2 2-4-4-5 5-1-1 5-5-4-4 2-2 4 1 4-4-1-3z" fill="#0f2760"/></symbol>
    <symbol id="i-pushpin-w" viewBox="0 0 24 24"><path d="M14 2l8 8-2 1-3-1-4 4 1 4-2 2-4-4-5 5-1-1 5-5-4-4 2-2 4 1 4-4-1-3z" fill="#fff"/></symbol>
    <symbol id="i-clock" viewBox="0 0 24 24"><circle cx="12" cy="12" r="9" fill="none" stroke="#0f2760" stroke-width="2.2"/><path d="M12 6.5V12l3.5 2.5" fill="none" stroke="#0f2760" stroke-width="2.2" stroke-linecap="round"/></symbol>
    <symbol id="i-pin" viewBox="0 0 24 24"><path d="M12 2a7 7 0 0 0-7 7c0 5 7 13 7 13s7-8 7-13a7 7 0 0 0-7-7z" fill="none" stroke="#0f2760" stroke-width="2.2"/><circle cx="12" cy="9" r="2.6" fill="#0f2760"/></symbol>
    <symbol id="i-lock" viewBox="0 0 24 24"><path d="M8 10V7a4 4 0 0 1 8 0" fill="none" stroke="#fff" stroke-width="2.4"/><rect x="5" y="10" width="14" height="12" rx="1.5" fill="#fff"/><circle cx="12" cy="16" r="2" fill="#8c949c"/></symbol>
    <symbol id="i-plus" viewBox="0 0 18 18"><path d="M9 2v14M2 9h14" stroke="#fff" stroke-width="2.4"/></symbol>
    <symbol id="i-back" viewBox="0 0 8 12"><path d="M7 1 2 6l5 5" fill="none" stroke="#0f2760" stroke-width="2"/></symbol>
    <symbol id="i-search" viewBox="0 0 30 30"><circle cx="12" cy="12" r="8.5" fill="none" stroke="#fff" stroke-width="3.4"/><path d="M18.5 18.5 27 27" stroke="#fff" stroke-width="3.8" stroke-linecap="round"/></symbol>
    <symbol id="i-tick" viewBox="0 0 34 34"><path d="M4 17l9 9L30 8" fill="none" stroke="#0d2a78" stroke-width="3.4"/></symbol>
    <symbol id="i-cross" viewBox="0 0 34 34"><path d="M6 6l22 22M28 6 6 28" stroke="#fff" stroke-width="3.4"/></symbol>
    <symbol id="i-shift" viewBox="0 0 18 18"><path d="M9 2 2 9h4v6h6V9h4z" fill="none" stroke="#fff" stroke-width="1.5"/></symbol>
    <symbol id="i-delete" viewBox="0 0 18 18"><path d="M6 3h10v12H6L1 9z" fill="none" stroke="#fff" stroke-width="1.5"/><path d="M9 6.5l4 5M13 6.5l-4 5" stroke="#fff" stroke-width="1.5"/></symbol>
    <symbol id="i-smile" viewBox="0 0 18 18"><circle cx="9" cy="9" r="7" fill="none" stroke="#fff" stroke-width="1.5"/><path d="M5.5 10.5a4 4 0 0 0 7 0" fill="none" stroke="#fff" stroke-width="1.5"/></symbol>
    <symbol id="i-mic" viewBox="0 0 18 18"><rect x="6.5" y="1.5" width="5" height="9" rx="2.5" fill="#fff"/><path d="M4 8.5a5 5 0 0 0 10 0M9 13.5v3" fill="none" stroke="#fff" stroke-width="1.5"/></symbol>
  </defs>
</svg>

<!-- Active tasks -->
<section class="screen s1">
  <div class="status"><span>●●●○○ phone</span><span>4:21 PM</span><span>100%</span></div>
  <header class="header">
    <div class="avatar" role="img" aria-label="User profile photo"></div>
    <div class="user-name">Daniel Morrow</div>
    <div class="user-place">Harlowmere, United Kingdom</div>
  </header>
  <div class="fab"><svg><use href="#i-plus"/></svg></div>
  <nav class="nav" style="top:118px">
    <span class="nav-back"><svg><use href="#i-back"/></svg>Back</span>
    <span class="nav-title">ACTIVE TASKS</span>
  </nav>
  <div class="task-list">
    <div class="task" style="height:62px">
      <svg class="task-play"><use href="#i-play"/></svg>
      <span class="task-label">01 Task</span>
      <div class="task-icons"><svg class="ic ic-a"><use href="#i-pushpin"/></svg><svg class="ic ic-b"><use href="#i-clock"/></svg><svg class="ic ic-c"><use href="#i-pin"/></svg></div>
    </div>
    <div class="task is-running" style="height:83px">
      <span class="task-stop"></span>
      <svg class="task-pause"><use href="#i-pause"/></svg>
      <span class="task-label">01 Task</span>
      <span class="task-timer">00:15:30</span>
      <div class="task-icons"><svg class="ic ic-c"><use href="#i-pin"/></svg></div>
    </div>
    <div class="task" style="height:81px">
      <svg class="task-play"><use href="#i-play"/></svg>
      <span class="task-label">01 Task</span>
      <div class="task-icons"><svg class="ic ic-a"><use href="#i-pushpin"/></svg><svg class="ic ic-c"><use href="#i-pin"/></svg></div>
    </div>
    <div class="task" style="height:85px">
      <svg class="task-play"><use href="#i-play"/></svg>
      <span class="task-label">01 Task</span>
      <div class="task-icons"><svg class="ic ic-a"><use href="#i-pushpin"/></svg><svg class="ic ic-b"><use href="#i-clock"/></svg></div>
    </div>
    <div class="task" style="height:62px;border-bottom:0">
      <svg class="task-play"><use href="#i-play"/></svg>
      <span class="task-label">01 Task</span>
      <div class="task-icons"><svg class="ic ic-a"><use href="#i-pushpin"/></svg><svg class="ic ic-b"><use href="#i-clock"/></svg><svg class="ic ic-c"><use href="#i-pin"/></svg></div>
    </div>
  </div>
  <div class="search-bar"><svg><use href="#i-search"/></svg></div>
</section>

<!-- New profile -->
<section class="screen s2">
  <div class="status"><span>●●●○○ phone</span><span>4:21 PM</span><span>100%</span></div>
  <header class="header">
    <div class="avatar" role="img" aria-label="User profile photo"></div>
    <div class="user-name">Daniel Morrow</div>
    <div class="user-place">Harlowmere, United Kingdom</div>
  </header>
  <div class="fab"><svg><use href="#i-plus"/></svg></div>
  <nav class="nav" style="top:118px">
    <span class="nav-back"><svg><use href="#i-back"/></svg>Back</span>
    <span class="nav-title">NEW PROFILE</span>
  </nav>
  <div class="field field-profile">Enter Profile Name</div>
  <div class="section-title">Choose Profile Tiggers</div>
  <div class="tabs"><div class="tab tab-on">Location</div><div class="tab tab-off">Time</div></div>
  <span class="option" style="top:322px">Time Tigger</span>
  <span class="toggle toggle-on" style="top:324px"></span>
  <span class="option" style="top:381px">Set Start Date</span>
  <span class="toggle toggle-off" style="top:379px"></span>
  <span class="option" style="top:435px">Repeat Every</span>
  <span class="option" style="top:494px">Between</span>
  <span class="line" style="left:90px;top:509px;width:68px"></span>
  <span class="option" style="left:163px;top:494px">and</span>
  <span class="line" style="left:197px;top:509px;width:70px"></span>
  <div class="action-bar" style="top:523px">
    <div class="action action-ok"><svg><use href="#i-tick"/></svg></div>
    <div class="action action-cancel"><svg><use href="#i-cross"/></svg></div>
  </div>
</section>

<!-- Location radius -->
<section class="screen s3">
  <div class="action-bar" style="top:0;height:56px">
    <div class="action action-ok"><svg><use href="#i-tick"/></svg></div>
    <div class="action action-cancel"><svg><use href="#i-cross"/></svg></div>
  </div>
  <div class="map" role="img" aria-label="Map of the selected region for the location trigger"></div>
  <div class="radius-bar">
    <span class="radius-label">Tigger Radious</span>
    <span class="slider"><span class="slider-fill"></span><span class="slider-knob"></span></span>
    <span class="radius-value">9.9 Km</span>
  </div>
</section>

<!-- New task -->
<section class="screen s4">
  <div class="status"><span>●●●○○ phone</span><span>4:21 PM</span><span>100%</span></div>
  <header class="header">
    <div class="avatar" role="img" aria-label="User profile photo"></div>
    <div class="user-name">Daniel Morrow</div>
    <div class="user-place">Harlowmere, United Kingdom</div>
  </header>
  <div class="spacer-band"></div>
  <div class="fab"><svg><use href="#i-plus"/></svg></div>
  <nav class="nav" style="top:187px">
    <span class="nav-back"><svg><use href="#i-back"/></svg>Back</span>
    <span class="nav-title">NEW TASK</span>
  </nav>
  <div class="field field-task">Name of a Task</div>
  <div class="rule"></div>
  <span class="option" style="left:27px;top:302px">Select Profile</span>
  <div class="profile-pick pick-pin"><svg><use href="#i-pushpin-w"/></svg></div>
  <div class="profile-pick pick-lock"><svg><use href="#i-lock"/></svg></div>
  <div class="keyboard">
    <div class="key-row"><span class="key">q</span><span class="key">w</span><span class="key">e</span><span class="key">r</span><span class="key">t</span><span class="key">y</span><span class="key">u</span><span class="key">i</span><span class="key">o</span><span class="key">p</span></div>
    <div class="key-row"><span class="key">a</span><span class="key">s</span><span class="key">d</span><span class="key">f</span><span class="key">g</span><span class="key">h</span><span class="key">j</span><span class="key">k</span><span class="key">l</span></div>
    <div class="key-row" style="gap:5px"><span class="key key-wide" style="margin-right:6px"><svg><use href="#i-shift"/></svg></span><span class="key">z</span><span class="key">x</span><span class="key">c</span><span class="key">v</span><span class="key">b</span><span class="key">n</span><span class="key">m</span><span class="key key-wide" style="margin-left:6px"><svg><use href="#i-delete"/></svg></span></div>
    <div class="key-row"><span class="key">123</span><span class="key"><svg><use href="#i-smile"/></svg></span><span class="key"><svg><use href="#i-mic"/></svg></span><span class="key key-space">space</span><span class="key key-return">return</span></div>
  </div>
</section>

</body>
</html>
```